Buch-/eBook-Cover für populär-wissenschaftliches Buch
Zielgruppe
Der Talgrund-Verlag veröffentlicht Bücher zu psychologischen Themen. Dies ist ein eher populär wissenschaftliches Buch für eine breite Leserschaft.
Aufgabenstellung
Benötigt wird ein Buchcover für KTZ, Papierformat 158*223, Buchformat 154 x 3 x 217 mm 272 Normseiten
Kurzbeschreibung
Am Ufer getragen?
Fragen sich die Autoren Konrad Brüning und Matthias Oswerk. Zwei Psychoanalytiker mit langer Berufserfahrung. Geht das überhaupt: in Liebe und vereint zu sein? Dazu müssen zunächst andere Fragen geklärt werden.
Was vereint die Geschlechter, was bringt sie zusammen? Liebe? Dieses Wort gab es im Deutschen im frühen Mittelalter nicht, erst im späteren. In manchen Kulturen gibt es dieses Wort bis heute nicht, und dennoch leben Mann und Frau zusammen. Schon seit Jahrtausenden beschäftigt sich der Mensch mit der Beziehung zwischen den Geschlechtern. Philosophen, Schriftsteller, Dichter, Maler, Musiker, später Psychoanalytiker, Anthropologen und Soziologen hat die Beziehung zwischen Mann und Frau intensiv beschäftigt. Auch die Religionen befassen sich mit der Beziehung zwischen den Geschlechtern und zeigen vorwiegend auf moralischen und idealistischen Ebenen Umgangsweisen und Lebensformen zwischen den Geschlechtern auf.
280 Normseiten
Bitte Klappentext auf Rückseite

```html
<!DOCTYPE html>
<html lang="de">
<head>
<meta charset="utf-8">
<title>Am Ufer getragen? – Umschlag</title>
<link href="https://fonts.googleapis.com/css2?family=Baloo+2:wght@600;700&family=Hind:wght@300;400;600&display=swap" rel="stylesheet">
<style>
  :root {
    --paper: #ffffff;
    --stage: #ffffff;
    --ink: #111111;
    --sky-light: #d9f0fb;
    --sky: #8fd2f0;
    --sky-deep: #5cbde8;
    --heart: #e5566b;
    --spine-line: #d8d8d8;
  }
  * { margin: 0; padding: 0; box-sizing: border-box; }
  html, body { width: 1200px; height: 632px; overflow: hidden; background: var(--stage); }
  body { font-family: "Hind", sans-serif; color: var(--ink); position: relative; }

  .spread {
    position: absolute; left: 165px; top: 16px;
    width: 870px; height: 600px;
    background: var(--paper);
    box-shadow: 0 2px 10px rgba(0,0,0,.12);
    display: flex;
  }
  .panel { position: relative; height: 100%; overflow: hidden; }
  .panel--back { width: 406px; }
  .panel--spine { width: 58px; border-left: 1px solid var(--spine-line); border-right: 1px solid var(--spine-line); }
  .panel--front { width: 406px; }

  .sky-band {
    position: absolute; left: 0; top: 0; width: 100%; height: 48px;
    background: linear-gradient(90deg, var(--sky-deep), var(--sky) 55%, var(--sky-light));
  }

  /* back */
  .back-title {
    position: absolute; top: 62px; left: 0; width: 100%;
    text-align: center; font-family: "Baloo 2", sans-serif; font-weight: 700; font-size: 20px;
  }
  .blurb {
    position: absolute; top: 104px; left: 40px; width: 330px;
    text-align: center; font-size: 10px; line-height: 14.8px;
  }
  .blurb p { margin-bottom: 8px; }
  .blurb .lead { font-weight: 600; }
  .authors-head { margin-top: 22px; margin-bottom: 6px; font-size: 9px; }
  .author { font-size: 9px; line-height: 13px; margin-bottom: 7px; }
  .author b { font-weight: 600; }

  .heart { position: absolute; fill: var(--heart); }

  /* spine */
  .spine-title {
    position: absolute; left: 2px; bottom: 220px;
    transform-origin: left bottom; transform: rotate(-90deg) translate(0, 100%);
    white-space: nowrap; font-family: "Baloo 2", sans-serif; font-weight: 700; font-size: 30px; line-height: 32px;
  }
  .spine-sub {
    position: absolute; left: 36px; bottom: 220px;
    transform-origin: left bottom; transform: rotate(-90deg) translate(0, 100%);
    white-space: nowrap; font-size: 11px; font-weight: 600; letter-spacing: .8px; line-height: 14px;
  }
  .spine-authors {
    position: absolute; top: 482px; left: 0; width: 100%;
    text-align: center; font-size: 11px; line-height: 11px; font-weight: 400;
  }

  /* front */
  .front-authors {
    position: absolute; top: 14px; left: 0; width: 100%; text-align: center;
    font-size: 21px; font-weight: 300; letter-spacing: .3px; line-height: 26px;
  }
  .front-title {
    position: absolute; top: 56px; left: 0; width: 100%; text-align: center;
    font-family: "Baloo 2", sans-serif; font-weight: 700; font-size: 39px; line-height: 52px;
  }
  .cover-photo {
    position: absolute; left: 0; top: 118px; width: 100%; height: 482px;
    background:
      radial-gradient(ellipse at 30% 35%, rgba(180,120,100,.75), transparent 45%),
      radial-gradient(ellipse at 75% 30%, rgba(235,200,180,.8), transparent 45%),
      radial-gradient(ellipse at 50% 90%, rgba(230,90,80,.55), transparent 50%),
      linear-gradient(180deg, var(--sky) 0%, var(--sky-light) 55%, #e8d6c8 100%);
  }
  .subtitle-tab {
    position: absolute; left: 0; top: 514px; width: 272px; height: 47px;
    background: var(--paper);
    clip-path: polygon(0 0, 92% 0, 100% 100%, 0 100%);
    padding: 5px 0 0 44px;
    font-size: 16px; font-weight: 600; letter-spacing: 1.4px; line-height: 18px;
  }
</style>
</head>
<body>
  <div class="spread">
    <section class="panel panel--back">
      <div class="sky-band"></div>
      <h2 class="back-title">Am Ufer getragen?</h2>
      <svg class="heart" style="left:302px;top:62px" width="22" height="16" viewBox="0 0 22 16"><path d="M1 15 L14 6" stroke="#e5566b" stroke-width="1.5"/><path d="M17 1c2-1 4 1 3 3l-3 4-4-3c-1-2 1-4 3-3z"/></svg>
      <svg class="heart" style="left:30px;top:124px" width="34" height="34" viewBox="0 0 24 24"><path d="M12 21 3 12.5C.5 10 1 5.5 4.5 4.5 7 3.8 9 5 12 8c3-3 5-4.2 7.5-3.5C23 5.5 23.5 10 21 12.5z"/></svg>
      <div class="blurb">
        <p><span class="lead">Fragen sich die Autoren Konrad Brüning und Matthias Oswerk.</span><br>
        Zwei Psychoanalytiker mit langer Berufserfahrung.<br>
        Geht das überhaupt: in Liebe und vereint zu sein?<br>
        Dazu müssen zunächst andere Fragen geklärt werden.</p>
        <p>Was vereint die Geschlechter, was bringt sie zusammen? Liebe? Dieses Wort gab es im Deutschen im frühen Mittelalter nicht, erst im späteren. In manchen Kulturen gibt es dieses Wort bis heute nicht, und dennoch leben Mann und Frau zusammen. Schon seit Jahrtausenden beschäftigt sich der Mensch mit der Beziehung zwischen den Geschlechtern.</p>
        <p>Philosophen, Schriftsteller, Dichter, Maler, Musiker, später Psychoanalytiker, Anthropologen und Soziologen hat die Beziehung zwischen Mann und Frau intensiv beschäftigt. Auch die Religionen befassen sich mit der Beziehung zwischen den Geschlechtern und zeigen vorwiegend auf moralischen und idealistischen Ebenen Umgangsweisen und Lebensformen zwischen den Geschlechtern auf.</p>
        <p class="authors-head">DIE AUTOREN:</p>
        <p class="author"><b>KONRAD BRÜNING</b> ist Diplom-Psychologe, Sozialwissenschaftler, Psychoanalytiker, Familientherapeut, Paartherapeut in eigener Praxis sowie Journalist und Filmemacher. Seit Jahren beforscht er die kulturellen Unterschiede in den Geschlechter und Familienbeziehungen verschiedener Kulturen (unter anderem in Ladakh, Himachal Pradesh, Namibia).</p>
        <p class="author"><b>MATTHIAS OSWERK</b> ist Facharzt für Psychotherapeutische Medizin und Psychoanalytiker. Er erforscht seit Jahren nach ethnoanalytischen Kriterien die Mosuo in China, eine der letzten matriarchalen Ethnien dieser Welt. Er erhielt den Prof. h.c. an der Qinglan-Universität Hebai.</p>
      </div>
      <svg class="heart" style="left:68px;top:518px" width="24" height="14" viewBox="0 0 24 14"><path d="M23 1 8 8" stroke="#e5566b" stroke-width="1.5"/><circle cx="5" cy="9" r="4"/></svg>
      <svg class="heart" style="left:110px;top:532px" width="14" height="24" viewBox="0 0 14 24"><path d="M3 23 9 6" stroke="#e5566b" stroke-width="1.5"/><circle cx="9" cy="5" r="4"/></svg>
      <svg class="heart" style="left:300px;top:518px" width="26" height="12" viewBox="0 0 26 12"><path d="M1 5 18 7" stroke="#e5566b" stroke-width="1.5"/><circle cx="21" cy="7" r="4"/></svg>
    </section>

    <section class="panel panel--spine">
      <div class="sky-band"></div>
      <div class="spine-title">Am Ufer getragen?</div>
      <div class="spine-sub">Psychologische Fragen und Hintergründe</div>
      <div class="spine-authors">BRÜNING<br>&amp;<br>OSWERK</div>
      <svg class="heart" style="left:15px;top:540px" width="28" height="28" viewBox="0 0 24 24"><path d="M12 21 3 12.5C.5 10 1 5.5 4.5 4.5 7 3.8 9 5 12 8c3-3 5-4.2 7.5-3.5C23 5.5 23.5 10 21 12.5z"/></svg>
    </section>

    <section class="panel panel--front">
      <div class="sky-band"></div>
      <div class="front-authors">BRÜNING &amp; OSWERK</div>
      <h1 class="front-title">Am Ufer getragen?</h1>
      <div class="cover-photo" role="img" aria-label="Farbiges Foto eines sich küssenden Paares vor blauem Himmel, durchsetzt mit bunten Wildblumen"></div>
      <svg class="heart" style="left:183px;top:100px;z-index:2" width="34" height="34" viewBox="0 0 24 24"><path d="M12 21 3 12.5C.5 10 1 5.5 4.5 4.5 7 3.8 9 5 12 8c3-3 5-4.2 7.5-3.5C23 5.5 23.5 10 21 12.5z"/></svg>
      <div class="subtitle-tab">Psychologische Fragen<br>und Hintergründe</div>
    </section>
  </div>
</body>
</html>
```